Business consultancy needs a greeting card (Thank you/gratitude) design

We need a Thank You card for a start up company located in Melbourne Australia. Part of the business is about learning to say thank you and being grateful so one of the products we will sell is a Thank you Card. We would like the design to be innovative, trendy, in line with our motto, "courage to make a difference" and business name/logo (Lantern Bloom which is about influencing others in a positive way which then continues to ripple on). By taking the effort of thanking people using a card is going the extra effort.
The design should include the Lantern Bloom colours (orange R250 g165 b65, blue R49 g 118 b192, purple r 183 g 165 b 210). Reference website: mylanternbloom.example Logo was uploaded but don't want part of the design, just as a reference. The card to be: trendy/make you feel happy. Would love some sort of "ripple".

Target Market(s)

Small businesses, individuals, younger generation

Industry/Entity Type

Business

• See logo. Use something trendy

Colors
876aae
f78f20
0555a3

Requirements
Must have
• trendy, creative, innovative. Use colours as seen in the project description. Add some sort of "ripple" (don't use water though)
Should not have
• Off the shelf type of look

```html
<!DOCTYPE html>
<html lang="en">
<head>
<meta charset="utf-8">
<title>Lantern Bloom — Thank You Card</title>
<link rel="stylesheet" href="https://fonts.googleapis.com/css2?family=Kalam:wght@400;700&display=swap">
<style>
  :root {
    --paper: #ffffff;
    --frame-purple: #cc99ff;
    --frame-orange: #ff9900;
    --frame-blue: #3366ff;
    --brand-orange: #fa8a3c;
    --brand-blue: #3a6ff0;
    --thanks-pink: #ff44cc;
    --thanks-lilac: #c9a6f0;
  }
  * { box-sizing: border-box; margin: 0; padding: 0; }
  html, body {
    width: 1200px;
    height: 804px;
    overflow: hidden;
    background: var(--paper);
  }
  .canvas {
    position: relative;
    width: 1200px;
    height: 804px;
    background: var(--paper);
  }
  .frame {
    position: absolute;
    left: 57px;
    top: 63px;
    width: 1088px;
    height: 676px;
    background: var(--frame-purple);
    padding: 17px;
  }
  .frame-orange {
    width: 100%;
    height: 100%;
    background: var(--frame-orange);
    padding: 17px;
  }
  .frame-blue {
    width: 100%;
    height: 100%;
    background: var(--frame-blue);
    padding: 17px;
  }
  .card-face {
    position: relative;
    width: 100%;
    height: 100%;
    background: var(--paper);
  }
  .motto {
    position: absolute;
    left: 0;
    right: 0;
    top: 34px;
    text-align: center;
    font-family: "Kalam", cursive;
    font-weight: 700;
    font-size: 54px;
    line-height: 1.2;
    letter-spacing: 1px;
    background: linear-gradient(180deg, var(--brand-orange) 25%, var(--brand-blue) 70%);
    -webkit-background-clip: text;
    background-clip: text;
    color: transparent;
  }
  .brand {
    position: absolute;
    left: 0;
    top: 150px;
    width: 100%;
    height: 130px;
  }
  .brand-dot {
    position: absolute;
    left: 70px;
    top: 8px;
    width: 130px;
    height: 120px;
    border-radius: 50%;
    background: var(--brand-orange);
  }
  .brand-name {
    position: absolute;
    left: 222px;
    top: 40px;
    font-family: "Kalam", cursive;
    font-weight: 700;
    font-size: 78px;
    line-height: 1;
    letter-spacing: 6px;
    text-transform: uppercase;
    color: var(--brand-blue);
  }
  .thanks {
    position: absolute;
    left: 290px;
    top: 410px;
    font-family: "Kalam", cursive;
    font-weight: 400;
    font-size: 108px;
    line-height: 1.1;
    background: linear-gradient(180deg, var(--frame-orange) 15%, var(--thanks-pink) 45%, var(--thanks-lilac) 75%);
    -webkit-background-clip: text;
    background-clip: text;
    color: transparent;
  }
</style>
</head>
<body>
  <main class="canvas">
    <section class="frame">
      <div class="frame-orange">
        <div class="frame-blue">
          <div class="card-face">
            <p class="motto">"Courage to make a Difference"</p>
            <div class="brand">
              <span class="brand-dot" aria-hidden="true"></span>
              <h1 class="brand-name">Lantern Bloom</h1>
            </div>
            <p class="thanks">Thank You</p>
          </div>
        </div>
      </div>
    </section>
  </main>
</body>
</html>
```